Borvel Stake Pool, redesign of existing website

Borvel is a stake pool that allow its users to stake their Marevo crypto to yearn stable yields. The existing site is at www.borvelstake.org The site is today is a little dull and I want to have suggestions for a redesign that makes the site stand out and that picks up the colors of the logo. I am not looking for a complete redesign, mainly colors and smaller changes to layout. Examples of sites to be inspired by www.quenda.network, https://app.tervalo.finance/

Target Market(s)

Crypto users on Marevo

Number of Pages Required

1 page

```html
<!DOCTYPE html>
<html lang="en">
<head>
<meta charset="utf-8">
<title>Borvel Stake – Liquid Staking on Marevo</title>
<link href="https://fonts.googleapis.com/css2?family=Figtree:wght@400;500;600;700;800&display=swap" rel="stylesheet">
<style>
  :root {
    --brand-blue: #1697c3;
    --brand-orange: #f47023;
    --ink: #0f2a33;
    --text: #2b3a40;
    --muted: #8a969b;
    --line: #dfe4e7;
    --panel: #ffffff;
    --note-bg: #eef1f3;
    --chip-bg: #e6f1f6;
  }
  * { box-sizing: border-box; margin: 0; padding: 0; }
  html, body { width: 1200px; height: 675px; overflow: hidden; }
  body {
    font-family: "Figtree", sans-serif;
    color: var(--text);
    position: relative;
    background:
      radial-gradient(ellipse 520px 420px at 1150px 560px, rgba(250,200,170,0.35), transparent 70%),
      radial-gradient(ellipse 600px 380px at 640px 300px, rgba(200,230,240,0.45), transparent 70%),
      #fcfdfd;
  }
  .announce {
    position: absolute; left: 0; top: 0; width: 1200px; height: 52px;
    background: var(--brand-blue); color: #fff;
    display: flex; align-items: center; justify-content: center; gap: 14px;
    font-size: 12px;
  }
  .announce .pill {
    display: flex; align-items: center; gap: 12px;
    border: 1px solid rgba(255,255,255,0.85); border-radius: 20px;
    height: 29px; padding: 0 14px 0 17px; font-size: 12px; color: #fff;
  }
  .site-header {
    position: absolute; left: 0; top: 52px; width: 1200px; height: 69px;
    border-bottom: 1px solid #e8ecee; background: #fff;
  }
  .brand { position: absolute; left: 176px; top: 17px; display: flex; align-items: center; gap: 10px; }
  .brand .mark { width: 30px; height: 30px; border-radius: 50%; background: var(--brand-blue); }
  .brand .name { font-size: 24px; font-weight: 700; color: var(--ink); letter-spacing: -0.3px; }
  .main-nav a { position: absolute; top: 29px; font-size: 12px; color: var(--ink); text-decoration: none; }
  .btn-orange {
    background: var(--brand-orange); color: #fff; border-radius: 26px;
    display: flex; align-items: center; justify-content: center; gap: 7px;
  }
  .header-wallet { position: absolute; left: 887px; top: 16px; width: 140px; height: 37px; font-size: 12.5px; }
  .hero-title {
    position: absolute; left: 172px; top: 183px;
    font-size: 48px; font-weight: 800; line-height: 58px; color: var(--ink); letter-spacing: -0.5px;
  }
  .hero-title .accent { color: var(--brand-orange); }
  .hero-copy {
    position: absolute; left: 172px; top: 319px; width: 430px;
    font-size: 13.5px; line-height: 21px; color: var(--text);
  }
  .hero-cta {
    position: absolute; left: 172px; top: 406px; width: 197px; height: 45px;
    border: 1px solid var(--ink); border-radius: 24px;
    display: flex; align-items: center; justify-content: center; gap: 16px;
    font-size: 12px; color: var(--ink);
  }
  .stake-card {
    position: absolute; left: 643px; top: 185px; width: 392px; height: 355px;
    background: var(--panel); border-radius: 8px;
    box-shadow: 0 10px 40px rgba(20,60,80,0.08);
  }
  .tabs { position: absolute; left: 22px; top: 29px; width: 347px; height: 34px; display: flex; border: 1px solid var(--line); }
  .tabs span { flex: 1; display: flex; align-items: center; justify-content: center; font-size: 10.5px; color: var(--muted); font-weight: 500; }
  .tabs span + span { border-left: 1px solid var(--line); }
  .tabs .active { background: var(--brand-blue); color: #fff; font-weight: 600; }
  .amount-field {
    position: absolute; left: 22px; width: 347px; height: 34px;
    border: 1px solid var(--line); border-radius: 2px;
  }
  .amount-field .chip {
    position: absolute; left: 2px; top: 2px; width: 88px; height: 28px;
    background: var(--chip-bg); display: flex; align-items: center; gap: 8px; padding-left: 6px;
    font-size: 10.5px; color: var(--brand-blue);
  }
  .chip .token { width: 20px; height: 20px; border-radius: 50%; background: #101820; }
  .amount-field .value { position: absolute; right: 13px; top: 8px; font-size: 12px; color: var(--ink); }
  .balance-row { position: absolute; left: 22px; width: 347px; display: flex; justify-content: space-between; font-size: 8.5px; color: var(--muted); }
  .balance-row .links span { text-decoration: underline; margin-left: 4px; }
  .swap-arrow { position: absolute; left: 189px; top: 124px; }
  .apy-note {
    position: absolute; left: 22px; top: 212px; width: 348px; height: 39px;
    background: var(--note-bg); border-left: 2px solid var(--brand-blue);
    display: flex; align-items: center; gap: 10px; padding-left: 15px; font-size: 10.5px; color: var(--text);
  }
  .card-wallet { position: absolute; left: 22px; top: 266px; width: 347px; height: 37px; font-size: 12.5px; }
  .fee-row { position: absolute; left: 22px; top: 314px; width: 342px; display: flex; justify-content: space-between; font-size: 8.5px; color: var(--muted); }
  .deco { position: absolute; left: 0; top: 0; pointer-events: none; }
  .rocket-art {
    position: absolute; left: 1101px; top: 279px; width: 48px; height: 50px; border-radius: 50%;
    background: linear-gradient(135deg, #1ba3a8, #1697c3 60%, #f47023);
  }
  .chain-badge {
    position: absolute; left: 172px; top: 602px; width: 29px; height: 29px; border-radius: 50%;
    background: #101820; box-shadow: 0 8px 12px rgba(0,0,0,0.2);
  }
  .footer-links { position: absolute; top: 610px; left: 710px; display: flex; font-size: 11px; color: var(--ink); }
  .footer-links span.sep { margin: 0 13px; }
</style>
</head>
<body>
  <div class="announce">
    <span>Borvel Points system is live! Earn when using borvelMRV in Defi.</span>
    <span class="pill">Learn More
      <svg width="15" height="10" viewBox="0 0 15 10"><path d="M0 5h13M9 1l4 4-4 4" fill="none" stroke="#fff" stroke-width="1.3"/></svg>
    </span>
  </div>

  <header class="site-header">
    <div class="brand"><span class="mark"></span><span class="name">Borvel Stake</span></div>
    <nav class="main-nav">
      <a style="left:457px">Home</a>
      <a style="left:536px">Validation</a>
      <a style="left:636px">Points</a>
      <a style="left:715px">Docs</a>
    </nav>
    <div class="btn-orange header-wallet">
      <svg width="17" height="15" viewBox="0 0 17 15"><rect x="1" y="4" width="15" height="10" rx="2" fill="none" stroke="#fff" stroke-width="1.2"/><path d="M3 4l8-3 1 3M11 8h5v3h-5z" fill="none" stroke="#fff" stroke-width="1.2"/></svg>
      Connect Wallet
    </div>
  </header>

  <svg class="deco" width="1200" height="675" viewBox="0 0 1200 675">
    <path d="M641 484 C560 455 450 470 426 560 C412 615 440 650 470 675" fill="none" stroke="#b9c4c8" stroke-width="1" stroke-dasharray="4 4"/>
    <path d="M1039 399 L1102 331" fill="none" stroke="#c3ccd0" stroke-width="1" stroke-dasharray="4 4"/>
  </svg>

  <h1 class="hero-title">Liquid <span class="accent">Staking</span><br>on Marevo</h1>
  <p class="hero-copy">Borvel Stake Pool offers non-custodial staking. Stake your MRV to receive a liquid staking token, borvelMRV, that you can use in Defi on Marevo. When you hold and use borvelMRV you also earn points.</p>
  <div class="hero-cta">What is Liquid Staking?
    <svg width="15" height="11" viewBox="0 0 15 11"><path d="M0 5.5h13M9 1.5l4 4-4 4" fill="none" stroke="#0f2a33" stroke-width="1.3"/></svg>
  </div>

  <section class="stake-card">
    <div class="tabs"><span class="active">Stake</span><span>Unstake</span><span>Referral</span></div>

    <div class="amount-field" style="top:77px"><div class="chip"><span class="token"></span>MRV</div><span class="value">0</span></div>
    <div class="balance-row" style="top:117px"><span>Balance: 0 MRV</span><span class="links"><span>max</span><span>half</span></span></div>
    <svg class="swap-arrow" width="12" height="14" viewBox="0 0 12 14"><path d="M6 0v12M1 7l5 5 5-5" fill="none" stroke="#0f2a33" stroke-width="1.2"/></svg>

    <div class="amount-field" style="top:150px"><div class="chip"><span class="token"></span>borvelMRV</div><span class="value">0</span></div>
    <div class="balance-row" style="top:190px"><span>Balance: 0 MRV</span><span class="links"><span>max</span><span>half</span></span></div>

    <div class="apy-note">
      <svg width="13" height="12" viewBox="0 0 13 12"><path d="M6.5 0L13 12H0z" fill="#1697c3"/><rect x="6" y="4" width="1.2" height="4" fill="#fff"/><rect x="6" y="9" width="1.2" height="1.2" fill="#fff"/></svg>
      Current APY: 8.29% across 60 validators
    </div>

    <div class="btn-orange card-wallet">
      <svg width="17" height="15" viewBox="0 0 17 15"><rect x="1" y="4" width="15" height="10" rx="2" fill="none" stroke="#fff" stroke-width="1.2"/><path d="M3 4l8-3 1 3M11 8h5v3h-5z" fill="none" stroke="#fff" stroke-width="1.2"/></svg>
      Connect Wallet
    </div>
    <div class="fee-row"><span>Priority fees</span><span>Yes</span></div>
  </section>

  <div class="rocket-art" role="img" aria-label="Small rocket illustration in brand teal and orange"></div>
  <div class="chain-badge"></div>

  <nav class="footer-links">
    <span>defi</span><span class="sep">|</span>
    <span>docs</span><span class="sep" style="margin-left:2px">|</span>
    <span>validators</span><span class="sep">|</span>
    <span>points</span><span class="sep">|</span>
    <span>murmur</span><span class="sep">|</span>
    <span>chirpline</span>
  </nav>
</body>
</html>
```